Tequila Bottle Labels

We are a construction company that bottled our own tequila and would like a unique label for it! We already have our own company logo (linked below) and we want that logo somewhere on the bottle as well- it can be big or small. It was brewed & bottled in Southern California. Ideally it would have the year "2020," "Single Estate," & "100% Agave Azul" somewhere on the label.

Tequila / RMT / 2020

```html
<!DOCTYPE html>
<html lang="en">
<head>
<meta charset="utf-8">
<title>RMT Single Estate Tequila – Label</title>
<link href="https://fonts.googleapis.com/css2?family=Cinzel:wght@500;700;800&family=Playfair+Display:ital,wght@1,600&display=swap" rel="stylesheet">
<style>
  :root {
    --page-bg: #1c3455;
    --label-blue: #2f5f8c;
    --label-blue-deep: #234a70;
    --gold: #dcb86e;
    --gold-soft: #c9a45c;
    --agave-tone: #7f9a8a;
  }
  * { margin: 0; padding: 0; box-sizing: border-box; }
  html, body {
    width: 900px;
    height: 1200px;
    overflow: hidden;
    background: var(--page-bg);
  }
  .canvas {
    position: relative;
    width: 900px;
    height: 1200px;
    display: flex;
    align-items: center;
    justify-content: center;
  }
  .label {
    position: relative;
    width: 720px;
    height: 760px;
    background: radial-gradient(ellipse at 50% 40%, var(--label-blue) 0%, var(--label-blue-deep) 100%);
    color: var(--gold);
    text-align: center;
    font-family: "Cinzel", serif;
  }
  .label-frame {
    position: absolute;
    inset: 18px;
    border: 2px solid var(--gold-soft);
    pointer-events: none;
  }
  .brand-name {
    position: absolute;
    top: 56px;
    left: 0; right: 0;
    font-size: 46px;
    font-weight: 700;
    letter-spacing: 4px;
    line-height: 1;
  }
  .single-estate {
    position: absolute;
    top: 134px;
    left: 0; right: 0;
    font-size: 24px;
    font-weight: 500;
    letter-spacing: 6px;
  }
  .product-name {
    position: absolute;
    top: 168px;
    left: 0; right: 0;
    font-size: 132px;
    font-weight: 800;
    letter-spacing: 6px;
    line-height: 1;
  }
  .agave-line {
    position: absolute;
    top: 318px;
    left: 0; right: 0;
    display: flex;
    align-items: center;
    justify-content: center;
    gap: 20px;
    font-size: 28px;
    font-weight: 700;
    letter-spacing: 6px;
  }
  .agave-line .rule {
    width: 70px;
    height: 2px;
    background: var(--gold-soft);
  }
  .agave-art {
    position: absolute;
    top: 380px;
    left: 250px;
    width: 220px;
    height: 140px;
    background: radial-gradient(ellipse at 50% 70%, var(--agave-tone) 0%, rgba(127,154,138,0.25) 70%, transparent 100%);
  }
  .divider {
    position: absolute;
    top: 548px;
    left: 60px;
    right: 60px;
    height: 2px;
    background: var(--gold-soft);
  }
  .origin-row {
    position: absolute;
    top: 572px;
    left: 60px;
    right: 60px;
    display: flex;
    align-items: center;
    justify-content: center;
    gap: 30px;
  }
  .vintage {
    font-family: "Playfair Display", serif;
    font-style: italic;
    font-weight: 600;
    font-size: 48px;
  }
  .origin-row .vertical-rule {
    width: 2px;
    height: 82px;
    background: var(--gold-soft);
  }
  .origin {
    text-align: left;
    font-size: 25px;
    font-weight: 700;
    letter-spacing: 3px;
    line-height: 1.45;
  }
  .flourish {
    position: absolute;
    top: 680px;
    left: 300px;
    width: 120px;
    height: 26px;
    background: linear-gradient(90deg, transparent, rgba(220,184,110,0.45), transparent);
    border-radius: 13px;
  }
</style>
</head>
<body>
  <main class="canvas">
    <section class="label">
      <div class="label-frame"></div>
      <div class="brand-name">RMT</div>
      <div class="single-estate">SINGLE ESTATE</div>
      <h1 class="product-name">TEQUILA</h1>
      <div class="agave-line"><span class="rule"></span>100% AGAVE AZUL<span class="rule"></span></div>
      <div class="agave-art" role="img" aria-label="Engraved illustration of a blue agave plant"></div>
      <div class="divider"></div>
      <div class="origin-row">
        <span class="vintage">2020</span>
        <span class="vertical-rule"></span>
        <p class="origin">BREWED &amp; BOTTLED IN<br>SOUTHERN CALIFORNIA</p>
      </div>
      <div class="flourish" role="img" aria-label="Small decorative gold flourish"></div>
    </section>
  </main>
</body>
</html>
```